新しくオープンしたラーメン居酒屋の新メニューのチラシ制作をお願いします。
こだわりが強く、比較的高級なラーメン屋です。高級感のある本格的なデザイン、訴求力がありながらも上品なデザインを希望します。
サイズ:A4サイズ
ノビテルで入稿します。
編集できるイラストレーターとPDFファイルでの納品をお願いします。

イメージ通りでした。

この度はたくさんのご応募ありがとうございます。今後ともよろしくお願いいたします。

```html
<!DOCTYPE html>
<html lang="ja">
<head>
<meta charset="utf-8">
<title>鯛出汁塩山椒そば 夏季限定</title>
<link href="https://fonts.googleapis.com/css2?family=Shippori+Mincho:wght@500;700;800&family=Noto+Serif+JP:wght@400;600&display=swap" rel="stylesheet">
<style>
  :root {
    --paper: #ffffff;
    --mist: #e3edf5;
    --mist-deep: #bfd3e5;
    --band: #4f86b8;
    --band-dark: #3f74a6;
    --ink: #2d3a44;
    --white: #ffffff;
    --bowl: #e88a3c;
    --bowl-deep: #cf6d2c;
    --broth: #efe6d4;
    --sansho: #6d8a3a;
  }
  html, body { margin: 0; padding: 0; overflow: hidden; }
  body { width: 851px; height: 1200px; background: var(--paper); }
  .flyer {
    position: relative; width: 851px; height: 1200px; overflow: hidden;
    background: linear-gradient(180deg, var(--paper) 0%, var(--paper) 34%, var(--mist) 50%, var(--mist) 70%, var(--mist-deep) 100%);
    font-family: "Shippori Mincho", "Noto Serif JP", serif;
    color: var(--ink);
  }
  .wave-texture {
    position: absolute; left: 120px; top: 690px; width: 240px; height: 180px;
    background: radial-gradient(ellipse at 60% 50%, rgba(159,190,216,.45) 0%, rgba(159,190,216,0) 70%);
  }
  .dish-photo {
    position: absolute; z-index: 2; left: 128px; top: -57px; width: 610px; height: 610px; border-radius: 50%;
    background: radial-gradient(circle at 50% 55%, var(--broth) 0%, var(--broth) 40%, var(--bowl) 44%, var(--bowl) 82%, var(--bowl-deep) 100%);
  }
  .menu-band {
    position: absolute; z-index: 1; left: 357px; top: 540px; width: 148px; bottom: 0;
    background: linear-gradient(180deg, var(--band) 0%, var(--band-dark) 100%);
  }
  .vertical { position: absolute; z-index: 3; writing-mode: vertical-rl; white-space: nowrap; margin: 0; }
  .chilled {
    position: absolute; z-index: 3; left: 420px; top: 640px; margin: 0;
    color: var(--white); font-size: 28px; font-weight: 700; line-height: 1;
    display: flex; align-items: center; gap: 6px;
  }
  .chilled .mark {
    background: var(--white); color: var(--band-dark); padding: 5px 4px;
  }
  .season-badge {
    left: 378px; top: 640px; color: var(--white);
    font-size: 19px; letter-spacing: 6px; padding: 12px 3px;
    border: 1px solid rgba(255,255,255,.85); border-radius: 16px;
  }
  .dish-name {
    left: 424px; top: 700px; color: var(--white);
    font-size: 54px; font-weight: 800; letter-spacing: 2px; line-height: 1;
  }
  .price {
    left: 380px; top: 912px; color: var(--white);
    font-size: 30px; letter-spacing: 3px; text-orientation: upright; line-height: 1;
  }
  .price .unit { font-size: 17px; margin-bottom: 18px; }
  .description {
    left: 530px; top: 880px; font-size: 14px; line-height: 1.85; letter-spacing: 1px;
    font-family: "Noto Serif JP", serif;
  }
  .no-additives {
    left: 528px; top: 1072px; font-size: 13px; letter-spacing: 2px; line-height: 1;
    border: 1px solid var(--ink); padding: 8px 5px; font-family: "Noto Serif JP", serif;
  }
  .sansho-sprig {
    position: absolute; left: 695px; top: 930px; width: 140px; height: 240px;
    border-radius: 45% 55% 50% 50%;
    background: radial-gradient(ellipse at 50% 50%, rgba(109,138,58,.6) 0%, rgba(109,138,58,.22) 55%, rgba(109,138,58,0) 75%);
  }
</style>
</head>
<body>
<main class="flyer">
  <div class="wave-texture" role="img" aria-label="淡い青の水彩と青海波模様"></div>
  <div class="dish-photo" role="img" aria-label="オレンジの器に盛られた冷製鯛出汁塩山椒そばの写真（海老、トマト、青菜、海苔のせ）"></div>

  <section class="menu-band"></section>
  <p class="vertical season-badge">夏季限定</p>
  <p class="chilled"><span class="mark">冷</span><span>製</span></p>
  <h1 class="vertical dish-name">鯛出汁塩山椒そば</h1>
  <p class="vertical price"><span class="unit">一杯</span>¥1000</p>

  <p class="vertical description">鯛を香ばしく焼き上げ<br>丁寧に引いた黄金の出汁<br>山椒の清涼な香りを添え<br>冷たく仕立てた夏の麺<br>細麺によく絡む澄んだ塩<br>暑い日にこそ味わう一杯</p>
  <p class="vertical no-additives">化学調味料不使用</p>

  <div class="sansho-sprig" role="img" aria-label="青山椒の実と葉のイラスト"></div>
</main>
</body>
</html>
```